Design some Business Cards for Web Company (Vector / AI)

Need a business card design, front and back, standard size :

(US)
Bleed size: 95.25 × 57.15 mm (3.75 × 2.25 in) (1⁄8 in bleeds)
Standard cut size: 89 × 51 mm (3.5 × 2 in)

Horizontal or vertical (portrait or landscape) layouts are both fine and will be considered.

This contest is *guaranteed* a winner. View our past contests to verify we *always* award a winner, so design to win this!

If your work is compelling and well done, we will give you more work to follow - this is also something of a test to find a good designer for future projects.

This is for a web development company, offering web, mobile and app development. You can view the site here to get an idea of the culture and presentation of the company in general : [url removed, login to view]

You will see in the body text of the site that it is a fun / irreverent, but still professional company. The design should be smart and sleek. The cards are full color on both sides, use that in a clever way.

Attached is the current logo for you use. You will have to convert it into vector (very simple, few circles and a gradient).

The winner of this contest will be the one that presents the best design that follows these creative ideas.

```html
<!DOCTYPE html>
<html lang="en">
<head>
<meta charset="utf-8">
<title>Brightpane Business Cards</title>
<link href="https://fonts.googleapis.com/css2?family=Arimo:wght@400;700&display=swap" rel="stylesheet">
<style>
  :root {
    --stage: #e9e6e2;
    --card: #050505;
    --accent: #1ba9e1;
    --ink: #ffffff;
    --shadow: rgba(0, 0, 0, 0.35);
  }
  * { margin: 0; padding: 0; box-sizing: border-box; }
  html, body {
    width: 1200px;
    height: 1105px;
    overflow: hidden;
    background: var(--stage);
  }
  .stage {
    position: relative;
    width: 1200px;
    height: 1105px;
    font-family: "Arimo", Arial, sans-serif;
    color: var(--ink);
  }
  .card {
    position: absolute;
    width: 660px;
    height: 377px;
    background: var(--card);
    overflow: hidden;
    box-shadow: 6px 10px 22px var(--shadow);
  }
  .card-front { left: 60px; top: 130px; }
  .card-back { left: 480px; top: 600px; }

  .front-sweep {
    position: absolute;
    left: 0; top: 0;
    width: 660px; height: 377px;
  }
  .contact {
    position: absolute;
    right: 220px;
    top: 52px;
    text-align: right;
    font-size: 20px;
    line-height: 1.12;
    text-transform: uppercase;
    letter-spacing: 0.2px;
  }
  .contact .name-block { margin-bottom: 42px; }
  .contact .address { margin-bottom: 42px; }
  .contact .lines { text-transform: none; }

  .brand {
    position: absolute;
    display: flex;
    align-items: center;
    gap: 8px;
    font-weight: 700;
    font-size: 19px;
    letter-spacing: 0.5px;
    text-transform: uppercase;
    color: var(--ink);
  }
  .brand-mark {
    width: 14px;
    height: 14px;
    background: var(--accent);
  }
  .card-front .brand { left: 462px; top: 150px; }
  .card-back .brand { right: 48px; bottom: 96px; }
</style>
</head>
<body>
<main class="stage">
  <section class="card card-front">
    <svg class="front-sweep" viewBox="0 0 660 377" aria-hidden="true">
      <path d="M0 0 H86 C66 130 92 270 198 377 H0 Z" fill="var(--accent)"/>
    </svg>
    <div class="contact">
      <div class="name-block">
        <div class="person-name">Marcus Dalton</div>
        <div class="person-role">CEO</div>
      </div>
      <div class="address">
        <div>418 Larkspur Avenue</div>
        <div>Fairview TX 75069</div>
      </div>
      <div class="lines">
        <div>marcus.dalton@brightpane.com</div>
        <div>+(555) 2910437 (555) 016 3382</div>
        <div>www.brightpane.com</div>
      </div>
    </div>
    <div class="brand"><span class="brand-mark"></span><span class="brand-name">Brightpane</span></div>
  </section>

  <section class="card card-back">
    <div class="brand"><span class="brand-mark"></span><span class="brand-name">Brightpane</span></div>
  </section>
</main>
</body>
</html>
```